Tamrock Stationery Design Project

company name : Tamrock General Trading LLC.
light watermark taken from the logo to cover almost the middle of the stationary..
logo is attached and an on going business card project is released on the same company name..
thanks
Reason: more time for more designs and to work with comfort..
Industry/Entity Type
Business
Colors
Designer to choose colors to be used in the design.
Look and feel
Each slider illustrates characteristics of the customer's brand and the style your logo design should communicate.

```html
<!DOCTYPE html>
<html lang="en">
<head>
<meta charset="utf-8">
<title>Corvane General Trading LLC — Letterhead</title>
<link rel="stylesheet" href="https://fonts.googleapis.com/css2?family=Cinzel:wght@400;600&family=Open+Sans:wght@400&display=swap">
<style>
  :root {
    --paper: #ffffff;
    --ink-grey: #949494;
    --ink-soft: #9a9a9a;
    --icon-blue: #2f80c6;
    --wave-light: #06b1dc;
    --wave-mid: #1687c0;
    --wave-steel: #1b6aab;
    --wave-deep: #224793;
    --mark-white: #ffffff;
  }
  * { margin: 0; padding: 0; box-sizing: border-box; }
  html, body {
    width: 927px;
    height: 1200px;
    overflow: hidden;
    background: var(--paper);
  }
  .letterhead {
    position: relative;
    width: 927px;
    height: 1200px;
    background: var(--paper);
    overflow: hidden;
  }
  .company-name {
    position: absolute;
    top: 54px;
    right: 55px;
    text-align: right;
    font-family: "Cinzel", serif;
    font-weight: 400;
    font-size: 19px;
    line-height: 21px;
    letter-spacing: 0;
    color: var(--ink-grey);
  }
  .contact-list {
    position: absolute;
    top: 109px;
    right: 55px;
    width: 172px;
    list-style: none;
    font-family: "Open Sans", sans-serif;
    font-size: 13.5px;
    line-height: 16px;
    letter-spacing: 0.4px;
    color: var(--ink-soft);
  }
  .contact-item {
    position: relative;
    text-align: right;
    margin-bottom: 10px;
  }
  .contact-icon {
    position: absolute;
    left: 0;
    top: 1px;
    width: 15px;
    height: 15px;
    fill: var(--icon-blue);
  }
  .wave {
    position: absolute;
    left: 0;
    top: 0;
    width: 927px;
    height: 1200px;
  }
  .brand-name {
    position: absolute;
    right: 54px;
    top: 1088px;
    font-family: "Cinzel", serif;
    font-weight: 600;
    font-size: 31px;
    letter-spacing: 0.3px;
    color: var(--mark-white);
  }
</style>
</head>
<body>
<main class="letterhead">
  <h1 class="company-name">Corvane General<br>Trading LLC</h1>

  <ul class="contact-list">
    <li class="contact-item">
      <svg class="contact-icon" viewBox="0 0 24 24" aria-hidden="true"><path d="M6.6 10.8a15.1 15.1 0 0 0 6.6 6.6l2.2-2.2a1 1 0 0 1 1-.25 11.4 11.4 0 0 0 3.6.57 1 1 0 0 1 1 1V20a1 1 0 0 1-1 1A17 17 0 0 1 3 4a1 1 0 0 1 1-1h3.5a1 1 0 0 1 1 1c0 1.250.2 2.450.57 3.570a1 1 0 0 1-.25 1z"/></svg>
      (555) 014 2290
    </li>
    <li class="contact-item">
      <svg class="contact-icon" viewBox="0 0 24 24" aria-hidden="true"><path d="M3 5h18a1 1 0 0 1 1 1v12a1 1 0 0 1-1 1H3a1 1 0 0 1-1-1V6a1 1 0 0 1 1-1zm1 2.3V8l8 5 8-5v-.7l-8 5z"/></svg>
      info@corvanellc.com
    </li>
    <li class="contact-item">
      <svg class="contact-icon" viewBox="0 0 24 24" aria-hidden="true"><path d="M12 2a7 7 0 0 0-7 7c0 5 7 13 7 13s7-8 7-13a7 7 0 0 0-7-7zm0 9.5A2.5 2.5 0 1 1 12 6.5a2.5 2.5 0 0 1 0 5z"/></svg>
      48 Harbor St,<br>Easton MA
    </li>
  </ul>

  <svg class="wave" viewBox="0 0 612 792" preserveAspectRatio="none" aria-hidden="true">
    <defs>
      <linearGradient id="waveGradient" x1="0" y1="1" x2="1" y2="0.55">
        <stop offset="0" stop-color="var(--wave-light)"/>
        <stop offset="0.45" stop-color="var(--wave-mid)"/>
        <stop offset="0.75" stop-color="var(--wave-steel)"/>
        <stop offset="1" stop-color="var(--wave-deep)"/>
      </linearGradient>
    </defs>
    <path fill="url(#waveGradient)" d="M0,741 C30,718 92,707 140,733 C174,752 198,772 236,752 C302,714 382,620 454,590 C512,566 568,566 612,578 L612,792 L0,792 Z"/>
  </svg>

  <div class="brand-name">Corvane Int.</div>
</main>
</body>
</html>
```